BrawnCrate placard

I need a placard designed that will go in my monthly subscription boxes to describe the products inside. There must be space to write 3-5 sentences on each product.
the first area will be titled: For your flowing mane
2 for your macho glow
3 to keep you smelling macho
4 to keep you clanging and banging at the gym.
Placard will be 5inchs wide and 7inchs long

I have attached the logo and the website address must be used in the design brawncrates.com.

Target Market(s)

men between 20-50

Colors

Designer to choose colors to be used in the design.

Requirements
Must have
• My website address brawncrates.com
• 4 area to write 3-5 sentences
• 1 for your flowing mane
• 2to keep you smelling macho
• 3 to keep you clanging and banging at the gym
• 4 for your macho glow

```html
<!DOCTYPE html>
<html lang="en">
<head>
<meta charset="utf-8">
<title>BrawnCrate Placard</title>
<link href="https://fonts.googleapis.com/css2?family=Montserrat:wght@400;500&display=swap" rel="stylesheet">
<style>
  :root {
    --page-bg: #e9e6e1;
    --card-bg: #0f0d0e;
    --ink: #ffffff;
    --rule: rgba(255, 255, 255, 0.28);
    --navy: #23366e;
    --navy-deep: #141c38;
    --amber: #b8682a;
    --skin: #c79a7e;
  }
  html, body {
    margin: 0;
    padding: 0;
    width: 1200px;
    height: 1200px;
    overflow: hidden;
    background: var(--page-bg);
    font-family: "Montserrat", Arial, sans-serif;
    color: var(--ink);
  }
  .placard {
    position: absolute;
    left: 200px;
    top: 40px;
    width: 800px;
    height: 1120px;
    background: var(--card-bg);
    overflow: hidden;
  }
  .hero-photo {
    position: absolute;
    left: 360px;
    top: 0;
    width: 440px;
    height: 1120px;
    background:
      radial-gradient(ellipse 120px 110px at 150px 840px, rgba(184,104,42,0.45), rgba(184,104,42,0) 100%),
      radial-gradient(ellipse 150px 190px at 330px 200px, rgba(199,154,126,0.3), rgba(199,154,126,0) 100%),
      linear-gradient(90deg, rgba(15,13,14,0) 0%, rgba(20,28,56,0.55) 60%, var(--navy) 100%);
  }
  .guide-lines {
    position: absolute;
    left: 0;
    top: 0;
    width: 800px;
    height: 1120px;
  }
  .section-list {
    position: absolute;
    left: 0;
    top: 0;
    margin: 0;
    padding: 0;
    list-style: none;
  }
  .section-number {
    position: absolute;
    left: 64px;
    width: 48px;
    text-align: center;
    font-size: 28px;
    font-weight: 500;
    line-height: 1;
    transform: translate(-50%, -50%);
  }
  .section-title {
    position: absolute;
    left: 104px;
    white-space: nowrap;
    font-size: 24px;
    font-weight: 500;
    line-height: 1;
    transform: translateY(-50%);
  }
  .copy {
    position: absolute;
    left: 56px;
    margin: 0;
    font-size: 13.5px;
    font-weight: 500;
    line-height: 18px;
  }
  .copy-intro { top: 664px; width: 688px; }
  .copy-occasion { top: 800px; width: 360px; }
  .copy-gift { top: 890px; width: 360px; }
  .contact {
    position: absolute;
    left: 56px;
    top: 996px;
  }
  .contact-title {
    margin: 0;
    font-size: 21px;
    font-weight: 500;
    letter-spacing: 0.3px;
  }
  .contact-line {
    margin: 4px 0 0;
    font-size: 15px;
    font-weight: 500;
  }
  .website {
    position: absolute;
    right: 106px;
    top: 1006px;
    font-size: 24px;
    font-weight: 500;
    line-height: 32px;
  }
</style>
</head>
<body>
  <main class="placard">
    <div class="hero-photo" role="img" aria-label="Photo of a bearded man in a navy suit examining a bottle of amber fragrance held in his hand"></div>

    <svg class="guide-lines" viewBox="0 0 800 1120" aria-hidden="true">
      <g fill="none" stroke="#ffffff" stroke-width="2.5">
        <line x1="64" y1="0" x2="64" y2="56"/>
        <circle cx="64" cy="80" r="24"/>
        <circle cx="64" cy="220" r="24"/>
        <circle cx="64" cy="360" r="24"/>
        <circle cx="64" cy="500" r="24"/>
        <circle cx="718" cy="1022" r="24"/>
        <line x1="718" y1="1046" x2="718" y2="1120"/>
      </g>
      <g class="writing-rules" stroke="var(--rule)" stroke-width="1">
        <line x1="104" y1="122" x2="744" y2="122"/>
        <line x1="104" y1="148" x2="744" y2="148"/>
        <line x1="104" y1="174" x2="744" y2="174"/>
        <line x1="104" y1="200" x2="744" y2="200"/>

        <line x1="104" y1="262" x2="744" y2="262"/>
        <line x1="104" y1="288" x2="744" y2="288"/>
        <line x1="104" y1="314" x2="744" y2="314"/>
        <line x1="104" y1="340" x2="744" y2="340"/>

        <line x1="104" y1="402" x2="744" y2="402"/>
        <line x1="104" y1="428" x2="744" y2="428"/>
        <line x1="104" y1="454" x2="744" y2="454"/>
        <line x1="104" y1="480" x2="744" y2="480"/>

        <line x1="104" y1="542" x2="744" y2="542"/>
        <line x1="104" y1="568" x2="744" y2="568"/>
        <line x1="104" y1="594" x2="744" y2="594"/>
        <line x1="104" y1="620" x2="744" y2="620"/>
      </g>
      <g class="globe-icon" fill="none" stroke="#ffffff" stroke-width="1.8">
        <circle cx="718" cy="1022" r="14"/>
        <ellipse cx="718" cy="1022" rx="6" ry="14"/>
        <line x1="704" y1="1022" x2="732" y2="1022"/>
        <line x1="707" y1="1014" x2="729" y2="1014"/>
        <line x1="707" y1="1030" x2="729" y2="1030"/>
      </g>
    </svg>

    <ol class="section-list">
      <li><span class="section-number" style="top:82px">1</span><span class="section-title" style="top:80px">For your flowing mane</span></li>
      <li><span class="section-number" style="top:222px">2</span><span class="section-title" style="top:220px">For your macho glow</span></li>
      <li><span class="section-number" style="top:362px">3</span><span class="section-title" style="top:360px">To keep you smelling macho</span></li>
      <li><span class="section-number" style="top:502px">4</span><span class="section-title" style="top:500px">To keep you clanging and banging at the gym</span></li>
    </ol>

    <p class="copy copy-intro">BrawnCrate is a luxury box for the macho man in all of us. You will find the products are from a variety of prestige brands. Some of these brands are well known and others are newly launched. When you subscribe you will enjoy at least four new luxury products each month such as hair products for your flowing mane, skin care products to keep you macho glow, nutritional supplements to keep you clanging and banging at the gym, and a fragrance to keep you smelling macho!</p>

    <p class="copy copy-occasion">Make sure you check out or special occasion/ holiday edition boxes. They will be a great addition to your subscription or a gift needed for that special occasion.</p>

    <p class="copy copy-gift">A BrawnCrate subscription the perfect gift for the macho man in your life.<br>A guaranteed hit!</p>

    <div class="contact">
      <p class="contact-title">CONTACT US</p>
      <p class="contact-line">Toll Free: 1-866-555-0142 | info@brawncrates.com</p>
    </div>

    <div class="website">brawncrates.com</div>
  </main>
</body>
</html>
```